Fashion Label Startup Business Card Design

Maribel Quint is a startup fashion designer based on the Gold Coast in QLD Australia. Maribels label " Vorine by Quint " is based upon taking old world design techniques and infusing them modern twist. The card design should incorporate an old world theme using colours like mustard, ocha, black, white and elements of lace pattern.

Card Details:

Maribel Quint
Fashion Designer
P: 04 0152 6847
E: vorinebyquint@mailbrook.com
W: www.friendsnet.com/VOrineByQuint

```html
<!DOCTYPE html>
<html lang="en">
<head>
<meta charset="utf-8">
<title>Vorine by Quint — Business Card</title>
<link href="https://fonts.googleapis.com/css2?family=Libre+Baskerville:wght@400;700&display=swap" rel="stylesheet">
<style>
  :root {
    --backdrop: #e9e6e1;
    --label-green: #4e8a40;
    --lace-pale: #d9e0cc;
    --lace-mid: #a9bf98;
    --mustard: #f3d54a;
    --card-white: #f0f1f0;
    --ink-green: #3f7a33;
    --shadow: rgba(0, 0, 0, 0.22);
  }
  * { box-sizing: border-box; margin: 0; padding: 0; }
  html, body {
    width: 1200px;
    height: 1000px;
    overflow: hidden;
    background: var(--backdrop);
    font-family: "Libre Baskerville", "Times New Roman", serif;
  }
  .canvas {
    position: relative;
    width: 1200px;
    height: 1000px;
  }
  .card {
    position: absolute;
    width: 600px;
    height: 360px;
    border-radius: 26px;
    overflow: hidden;
    box-shadow: 0 10px 24px var(--shadow);
  }

  /* Front of the card */
  .card-front {
    left: 540px;
    top: 90px;
    background: var(--label-green);
  }
  .lace-frame {
    position: absolute;
    inset: 0;
    background:
      radial-gradient(ellipse at center, transparent 46%, rgba(217,224,204,0.55) 62%, rgba(169,191,152,0.75) 100%),
      var(--label-green);
  }
  .front-panel {
    position: absolute;
    left: 110px;
    top: 95px;
    width: 380px;
    height: 170px;
    border-radius: 40px;
    background: var(--label-green);
    display: flex;
    flex-direction: column;
    align-items: center;
    justify-content: center;
    color: var(--mustard);
    text-align: center;
  }
  .label-name {
    font-size: 46px;
    line-height: 1;
    white-space: nowrap;
  }
  .label-name .connector { font-size: 28px; }
  .label-name .surname { font-weight: 700; }
  .designer-name {
    margin-top: 14px;
    font-size: 19px;
  }
  .designer-role {
    margin-top: 4px;
    font-size: 14px;
  }

  /* Back of the card */
  .card-back {
    left: 60px;
    top: 560px;
    background: var(--card-white);
  }
  .corner-ornament {
    position: absolute;
    width: 170px;
    height: 170px;
    background: var(--ink-green);
  }
  .corner-ornament.top-left {
    left: 22px;
    top: 22px;
    clip-path: polygon(0 0, 100% 0, 0 100%);
  }
  .corner-ornament.bottom-right {
    right: 22px;
    bottom: 22px;
    clip-path: polygon(100% 0, 100% 100%, 0 100%);
  }
  .contact-list {
    position: absolute;
    left: 150px;
    top: 138px;
    width: 300px;
    display: flex;
    flex-direction: column;
    align-items: center;
    color: var(--ink-green);
    font-size: 16px;
  }
  .contact-line {
    display: flex;
    align-items: center;
    gap: 8px;
    white-space: nowrap;
  }
  .contact-line svg { flex: none; }
  .divider {
    width: 230px;
    height: 8px;
    margin: 12px 0;
    border-radius: 4px;
    background: linear-gradient(90deg, transparent 0, var(--mustard) 10%, var(--mustard) 90%, transparent 100%);
  }
</style>
</head>
<body>
<main class="canvas">

  <section class="card card-front" aria-label="Card front">
    <div class="lace-frame" role="img" aria-label="Pale lace pattern border framing the card"></div>
    <div class="front-panel">
      <h1 class="label-name">Vorine <span class="connector">by</span> <span class="surname">Quint</span></h1>
      <p class="designer-name">Maribel Quint</p>
      <p class="designer-role">Fashion Designer</p>
    </div>
  </section>

  <section class="card card-back" aria-label="Card back">
    <div class="corner-ornament top-left" role="img" aria-label="Green scrolling floral corner ornament"></div>
    <div class="corner-ornament bottom-right" role="img" aria-label="Green scrolling floral corner ornament"></div>

    <div class="contact-list">
      <p class="contact-line">
        <svg width="15" height="15" viewBox="0 0 24 24" aria-hidden="true"><path fill="currentColor" d="M6.6 10.8a15.1 15.1 0 0 0 6.6 6.6l2.2-2.2c.3-.3.7-.4 1-.2 1.1.4 2.3.6 3.6.6.6 0 1 .4 1 1V20c0 .6-.4 1-1 1A17 17 0 0 1 3 4c0-.6.4-1 1-1h3.5c.6 0 1 .4 1 1 0 1.3.2 2.5.6 3.6.1.3 0 .7-.2 1z"/></svg>
        <span>04 0152 6847</span>
      </p>
      <div class="divider" role="img" aria-label="Yellow pencil divider"></div>
      <p class="contact-line">
        <svg width="17" height="13" viewBox="0 0 24 18" aria-hidden="true"><rect x="1" y="1" width="22" height="16" fill="none" stroke="currentColor" stroke-width="2"/><path d="M1 1l11 9 11-9" fill="none" stroke="currentColor" stroke-width="2"/></svg>
        <span>vorinebyquint@mailbrook.com</span>
      </p>
      <div class="divider" role="img" aria-label="Yellow pencil divider"></div>
      <p class="contact-line">
        <svg width="16" height="16" viewBox="0 0 24 24" aria-hidden="true"><circle cx="12" cy="12" r="10" fill="currentColor"/><path d="M2 12h20M12 2c3 3 3 17 0 20M12 2c-3 3-3 17 0 20" fill="none" stroke="#f0f1f0" stroke-width="1.4"/></svg>
        <span>www.friendsnet.com/VOrineByQuint</span>
      </p>
    </div>
  </section>

</main>
</body>
</html>
```